Modern business cards and stationery design for an IT company
Brolund Systems
Modern business cards and stationery design for an IT company - Information Technology
Creative Brief
Professional
Tomas Ellery
President
We do not want our address on the business card
tomas@brolundsys.example
www.brolundsys.example
BrolundSys BrolundSys
For reference, please visit our new website which is currently being constructed located at www.brolundsys.example/tellery This website provides the new design and layout for the company and potentially will help with the design process. Please note that the main website (www.brolundsys.example) is in process of being replaced with the first website mentioned. (www.brolundsys.example/tellery).

```html
<!DOCTYPE html>
<html lang="en">
<head>
<meta charset="utf-8">
<title>Brolund Systems – Business Card</title>
<link href="https://fonts.googleapis.com/css2?family=Montserrat:wght@500;600;800&display=swap" rel="stylesheet">
<style>
  :root{
    --page:#e9e9ea;
    --card:#ffffff;
    --red-deep:#8e0c10;
    --red:#c8161c;
    --red-bright:#e2262b;
    --grey:#b9bbbe;
    --grey-light:#dcdddf;
    --ink:#1f1f21;
    --white:#ffffff;
  }
  *{margin:0;padding:0;box-sizing:border-box}
  html,body{width:1200px;height:901px;overflow:hidden;background:var(--page);font-family:"Montserrat",sans-serif}
  .business-card{
    position:absolute;left:100px;top:165px;width:1000px;height:570px;
    background:var(--card);border-radius:38px;overflow:hidden;
    box-shadow:0 18px 40px rgba(0,0,0,.18);
  }
  .card-waves{position:absolute;inset:0;width:100%;height:100%}
  .brand{position:absolute;left:80px;top:70px;display:flex;align-items:center;gap:16px}
  .brand-dot{width:46px;height:46px;border-radius:50%;background:var(--red)}
  .brand-name{font-weight:800;font-size:40px;letter-spacing:2px;color:var(--red);text-transform:uppercase;white-space:nowrap}
  .holder{position:absolute;left:80px;top:200px}
  .holder-name{font-weight:600;font-size:34px;letter-spacing:1px;color:var(--ink);text-transform:uppercase;white-space:nowrap}
  .holder-role{font-weight:500;font-size:24px;color:var(--red);margin-top:4px}
  .contacts{position:absolute;left:620px;top:335px;list-style:none}
  .contact{display:flex;align-items:center;gap:14px;height:40px;color:var(--white);font-size:20px;font-weight:500;white-space:nowrap}
  .contact-icon{width:26px;height:26px;flex:none}
</style>
</head>
<body>
  <section class="business-card">
    <svg class="card-waves" viewBox="0 0 1000 570" aria-hidden="true">
      <defs>
        <linearGradient id="redBand" x1="0" y1="1" x2="1" y2="0">
          <stop offset="0" stop-color="var(--red-deep)"/>
          <stop offset=".55" stop-color="var(--red)"/>
          <stop offset="1" stop-color="var(--red-bright)"/>
        </linearGradient>
        <linearGradient id="greyBand" x1="0" y1="0" x2="1" y2="0">
          <stop offset="0" stop-color="var(--grey-light)"/>
          <stop offset="1" stop-color="var(--grey)"/>
        </linearGradient>
      </defs>
      <path d="M0,290 C260,330 620,215 1000,140 L1000,235 C650,275 300,380 0,372 Z" fill="url(#greyBand)"/>
      <path d="M0,385 C300,400 660,280 1000,238 L1000,570 L0,570 Z" fill="url(#redBand)"/>
      <path d="M0,392 C300,408 660,290 1000,250" fill="none" stroke="var(--white)" stroke-width="5"/>
      <path d="M0,550 C340,550 720,520 1000,505" fill="none" stroke="var(--white)" stroke-opacity=".3" stroke-width="2"/>
    </svg>

    <div class="brand">
      <span class="brand-dot"></span>
      <span class="brand-name">Brolund Systems</span>
    </div>

    <div class="holder">
      <p class="holder-name">Tomas Ellery</p>
      <p class="holder-role">President</p>
    </div>

    <ul class="contacts">
      <li class="contact">
        <svg class="contact-icon" viewBox="0 0 26 26"><circle cx="13" cy="13" r="13" fill="var(--white)"/><path d="M9 7h3l1 4-2 1a8 8 0 0 0 3 3l1-2 4 1v3a2 2 0 0 1-2 2C11 19 7 15 7 9a2 2 0 0 1 2-2z" fill="var(--red)"/></svg>
        <span>012 555 0147</span>
      </li>
      <li class="contact">
        <svg class="contact-icon" viewBox="0 0 26 26"><circle cx="13" cy="13" r="13" fill="var(--white)"/><path d="M9 7h3l1 4-2 1a8 8 0 0 0 3 3l1-2 4 1v3a2 2 0 0 1-2 2C11 19 7 15 7 9a2 2 0 0 1 2-2z" fill="var(--red)"/></svg>
        <span>012 555 0183</span>
      </li>
      <li class="contact">
        <svg class="contact-icon" viewBox="0 0 26 26"><circle cx="13" cy="13" r="13" fill="var(--white)"/><rect x="6" y="8" width="14" height="10" rx="1" fill="var(--red)"/><path d="M6.5 8.5 13 14l6.5-5.5" fill="none" stroke="var(--white)" stroke-width="1.4"/></svg>
        <span>tomas@brolundsys.example</span>
      </li>
      <li class="contact">
        <svg class="contact-icon" viewBox="0 0 26 26"><circle cx="13" cy="13" r="13" fill="var(--white)"/><circle cx="13" cy="13" r="7" fill="none" stroke="var(--red)" stroke-width="1.6"/><ellipse cx="13" cy="13" rx="3" ry="7" fill="none" stroke="var(--red)" stroke-width="1.4"/><path d="M6 13h14" stroke="var(--red)" stroke-width="1.4"/></svg>
        <span>www.brolundsys.example</span>
      </li>
    </ul>
  </section>
</body>
</html>
```